Hot air balloon tour company needs a brochure redesign

Look for a fresh new brochure design. Using company logo and colours.
Modern, simple and professional look required
Font styles to use
Sans Serif
Colors
0054AA
0677BA
7BADD7
CADEEF
E8F1F8

```html
<!DOCTYPE html>
<html lang="en">
<head>
<meta charset="utf-8">
<title>Vellaray Ballooning – Tri-fold Brochure</title>
<link rel="stylesheet" href="https://fonts.googleapis.com/css2?family=Poppins:wght@400;500;600;700&display=swap">
<style>
:root{
  --blue-deep:#0054AA;
  --blue:#0677BA;
  --blue-soft:#7BADD7;
  --blue-pale:#CADEEF;
  --blue-mist:#E8F1F8;
  --accent:#1d9ad8;
  --ink:#1b1c1f;
  --paper:#ffffff;
  --stage:#d9dadb;
  --text-body:#3b3d42;
}
*{box-sizing:border-box;margin:0;padding:0}
html,body{width:1200px;height:2400px;overflow:hidden}
body{background:var(--stage);font-family:'Poppins',sans-serif;position:relative}
.spread{position:absolute;left:40px;width:1120px;height:866px;display:flex;box-shadow:0 14px 40px rgba(0,0,0,.25)}
.spread--outside{top:190px}
.spread--inside{top:1250px}
.panel{position:relative;width:373.33px;height:866px;overflow:hidden}
.panel--dark{background:var(--ink);color:#fff}
.panel--light{background:var(--paper);color:var(--text-body)}
.panel svg.bg{position:absolute;inset:0;width:100%;height:100%}
.layer{position:absolute;left:0;right:0}

.brand{display:flex;align-items:center;gap:10px;font-weight:600;color:var(--accent);line-height:1}
.brand__dot{width:24px;height:24px;border-radius:50%;background:var(--accent);flex:none}
.brand__name{font-size:28px;white-space:nowrap}
.brand--small .brand__name{font-size:23px}
.brand--small .brand__dot{width:20px;height:20px}
.brand--center{justify-content:center}

.pill{display:inline-block;background:var(--accent);color:#fff;border-radius:30px;font-weight:600}
.offer__title{width:240px;margin:0 auto;text-align:center;font-size:19px;padding:5px 0;letter-spacing:.5px}
.offer__list{list-style:none;text-align:right;padding-right:50px;margin-top:16px}
.offer__list li{font-size:15px;line-height:1.9;font-weight:500}
.offer__list li:nth-child(even){color:var(--accent)}

.tagline{font-size:23px;font-weight:500;line-height:1.3;text-align:center;color:#fff}
.phone-pill{display:flex;align-items:center;gap:10px;width:250px;margin:0 auto;background:var(--accent);border-radius:30px;padding:7px 16px;font-size:22px;font-weight:600;color:#fff}
.phone-icon{width:26px;height:26px;border-radius:50%;background:#fff;display:flex;align-items:center;justify-content:center;flex:none}

.blurb{font-size:14px;line-height:1.6;text-align:center;padding:0 34px}
.socials{display:flex;justify-content:center;gap:12px;margin-top:18px}
.socials span{width:26px;height:26px;border-radius:50%;border:2px solid #fff;display:block}
.hotline{text-align:center;margin-top:22px}
.hotline__label{font-size:15px;font-weight:600}
.hotline__big{font-size:36px;font-weight:700;line-height:1.1;white-space:nowrap}
.hotline__big em{font-style:normal;color:var(--accent)}
.hotline__num{font-size:18px;font-weight:600}
.web{font-size:15px;color:var(--accent);margin-top:6px;text-align:center;white-space:nowrap}

.feature{padding:0 30px;margin-bottom:18px}
.feature h3{font-size:17px;font-weight:600;color:var(--accent);line-height:1.3;margin-bottom:4px}
.feature p{font-size:13.5px;line-height:1.55}
.bar{position:absolute;left:0;right:0;bottom:30px;height:40px;background:var(--accent);display:flex;align-items:center;gap:10px;padding-left:26px;color:#fff;font-size:16px;font-weight:600;white-space:nowrap}
.bar--dark{background:var(--ink);left:26px;right:26px;border-radius:22px;padding-left:10px;font-size:15px}
.photo-ring{position:absolute;border-radius:50%;border:6px solid var(--accent)}
</style>
</head>
<body>

<section class="spread spread--outside">

  <article class="panel panel--dark">
    <svg class="bg" viewBox="0 0 373 866" preserveAspectRatio="none">
      <defs>
        <linearGradient id="flapPhoto" x1="0" y1="0" x2="1" y2="1">
          <stop offset="0" stop-color="#6c7f5a"/><stop offset=".5" stop-color="#b98a4f"/><stop offset="1" stop-color="#3c3a33"/>
        </linearGradient>
      </defs>
      <path d="M0 0H373V150C260 190 120 170 0 120Z" fill="#fff"/>
      <path d="M0 120C120 170 260 190 373 150" fill="none" stroke="var(--accent)" stroke-width="8"/>
      <g role="img" aria-label="Photo of guests smiling in a balloon basket">
        <path d="M0 640C110 600 220 610 373 670V866H0Z" fill="url(#flapPhoto)"/>
      </g>
      <path d="M0 640C110 600 220 610 373 670" fill="none" stroke="var(--accent)" stroke-width="8"/>
    </svg>
    <div class="layer" style="top:46px"><div class="brand brand--center"><span class="brand__dot"></span><span class="brand__name">Vellaray Ballooning</span></div></div>
    <div class="layer" style="top:210px">
      <div class="pill offer__title" style="display:block">WE OFFER</div>
      <ul class="offer__list">
        <li>Daily Flights over the Hunter Valley</li>
        <li>Champagne Breakfast</li>
        <li>Digital Flight Photos</li>
        <li>Corporate Flights</li>
        <li>Private Flights</li>
        <li>Gift Vouchers</li>
      </ul>
    </div>
    <div role="img" aria-label="Round photo of a balloon at sunrise" class="photo-ring" style="left:220px;top:570px;width:130px;height:130px;background:linear-gradient(160deg,#e9b56a,#5a4a3a)"></div>
  </article>

  <article class="panel panel--dark">
    <svg class="bg" viewBox="0 0 373 866" preserveAspectRatio="none">
      <path d="M300 0H373V866H340C360 700 380 300 300 0Z" fill="#fff"/>
      <path d="M300 0C380 300 360 700 340 866" fill="none" stroke="var(--accent)" stroke-width="8"/>
    </svg>
    <div role="img" aria-label="Round aerial photo of a balloon over green fields" class="photo-ring" style="left:100px;top:60px;width:170px;height:170px;background:radial-gradient(circle at 50% 45%,#8fb05a,#3f5a2c)"></div>
    <div class="layer" style="top:270px;right:30px"><div class="brand brand--center brand--small"><span class="brand__dot"></span><span class="brand__name">Vellaray Ballooning</span></div></div>
    <div class="layer" style="top:320px;right:30px">
      <p class="blurb" style="padding:0 24px">Experience Hunter Valley in the best way possible. For hot air balloon gifts or rides, go with Vellaray Ballooning</p>
      <div class="socials"><span></span><span></span><span></span><span></span></div>
      <div class="hotline">
        <div class="hotline__label">Booking Hot Line</div>
        <div class="hotline__big">1300 <em>UP HIGH</em></div>
        <div class="hotline__num">(1300 555 019)</div>
      </div>
      <div class="web">www.vellarayballooning.example</div>
    </div>
  </article>

  <article class="panel panel--light">
    <svg class="bg" viewBox="0 0 373 866" preserveAspectRatio="none">
      <defs>
        <linearGradient id="coverPhoto" x1="0" y1="0" x2="0" y2="1">
          <stop offset="0" stop-color="#8b9bb3"/><stop offset=".45" stop-color="#c9c2b8"/><stop offset=".7" stop-color="#9a7b5c"/><stop offset="1" stop-color="#3d3a3a"/>
        </linearGradient>
      </defs>
      <g role="img" aria-label="Photo of hot air balloons floating above a misty valley at sunrise">
        <path d="M0 170C120 150 250 150 373 120V600H0Z" fill="url(#coverPhoto)"/>
      </g>
      <path d="M0 600C140 520 260 480 373 470V866H0Z" fill="var(--ink)"/>
      <path d="M0 600C140 520 260 480 373 470" fill="none" stroke="var(--accent)" stroke-width="10"/>
      <path d="M0 170C120 150 250 150 373 120" fill="none" stroke="var(--blue-pale)" stroke-width="4"/>
    </svg>
    <div class="layer" style="top:50px"><div class="brand brand--center"><span class="brand__dot"></span><span class="brand__name">Vellaray Ballooning</span></div></div>
    <div class="layer" style="top:640px">
      <p class="tagline">Experience the<br>beautiful Hunter Valley<br>in a hot air balloon</p>
      <div style="height:28px"></div>
      <div class="phone-pill"><span class="phone-icon"><svg width="14" height="14" viewBox="0 0 24 24"><path d="M6.6 10.8a15 15 0 006.6 6.6l2.2-2.2a1 1 0 011-.25 11.4 11.4 0 003.6.57 1 1 0 011 1V20a1 1 0 01-1 1A17 17 0 013 4a1 1 0 011-1h3.5a1 1 0 011 1c0 1.25.2 2.45.57 3.57a1 1 0 01-.25 1z" fill="var(--ink)"/></svg></span>1300 555 019</div>
    </div>
  </article>
</section>

<section class="spread spread--inside">

  <article class="panel panel--dark">
    <svg class="bg" viewBox="0 0 373 866" preserveAspectRatio="none">
      <defs>
        <linearGradient id="valleyPhoto" x1="0" y1="0" x2="0" y2="1">
          <stop offset="0" stop-color="#a9b8c8"/><stop offset=".5" stop-color="#8c8f7d"/><stop offset="1" stop-color="#4d5a3e"/>
        </linearGradient>
      </defs>
      <g role="img" aria-label="Photo of three balloons over a green valley">
        <path d="M0 620C120 660 260 650 373 610V866H0Z" fill="url(#valleyPhoto)"/>
      </g>
      <path d="M0 620C120 660 260 650 373 610" fill="none" stroke="var(--accent)" stroke-width="8"/>
    </svg>
    <div class="layer" style="top:60px">
      <p class="tagline" style="font-size:24px">Experience the<br>beautiful Hunter Valley<br>in a hot air balloon</p>
      <p class="blurb" style="margin-top:30px;font-size:14.5px">Vellaray Ballooning is the Hunter Valley's premium hot air balloon flight company, catering for small or large groups with first class equipment and an experienced team. Vellaray Ballooning is a family business, locally owned and operated in the Hunter Valley.</p>
      <div class="hotline" style="margin-top:40px">
        <div class="hotline__label">Booking Hot Line</div>
        <div class="hotline__big">1300 <em>UP HIGH</em></div>
        <div class="hotline__num">(1300 555 019)</div>
      </div>
      <div class="web">www.vellarayballooning.example</div>
    </div>
  </article>

  <article class="panel panel--light">
    <svg class="bg" viewBox="0 0 373 866" preserveAspectRatio="none">
      <defs>
        <linearGradient id="midPhoto" x1="0" y1="0" x2="1" y2="1">
          <stop offset="0" stop-color="#6f7d8e"/><stop offset=".6" stop-color="#c99a62"/><stop offset="1" stop-color="#4b4a3a"/>
        </linearGradient>
      </defs>
      <g role="img" aria-label="Photo of a patterned balloon above hills at sunrise">
        <path d="M0 0H373V290C250 300 110 330 0 370Z" fill="url(#midPhoto)"/>
      </g>
      <path d="M0 370C110 330 250 300 373 290" fill="none" stroke="var(--accent)" stroke-width="10"/>
    </svg>
    <div class="layer" style="top:390px"><div class="brand brand--center"><span class="brand__dot"></span><span class="brand__name">Vellaray Ballooning</span></div></div>
    <div class="layer" style="top:450px">
      <div class="feature"><h3>Experienced Pilots &amp; Crew</h3><p>Our pilots and crew are fully trained professionals who fly under strict aviation safety rules, giving every guest a calm and memorable morning in the sky.</p></div>
      <div class="feature"><h3>Award Winning Service</h3><p>We are a locally owned business that has earned several regional tourism awards, and we aim to lead the industry in every part of the journey.</p></div>
    </div>
    <div class="bar"><span class="phone-icon"><svg width="14" height="14" viewBox="0 0 24 24"><path d="M6.6 10.8a15 15 0 006.6 6.6l2.2-2.2a1 1 0 011-.25 11.4 11.4 0 003.6.57 1 1 0 011 1V20a1 1 0 01-1 1A17 17 0 013 4a1 1 0 011-1h3.5a1 1 0 011 1c0 1.25.2 2.45.57 3.57a1 1 0 01-.25 1z" fill="var(--accent)"/></svg></span>1300 UP HIGH | (1300 555 019)</div>
  </article>

  <article class="panel panel--light">
    <svg class="bg" viewBox="0 0 373 866" preserveAspectRatio="none">
      <defs>
        <linearGradient id="sunPhoto" x1="0" y1="0" x2="0" y2="1">
          <stop offset="0" stop-color="#f0c27a"/><stop offset=".6" stop-color="#d08a4a"/><stop offset="1" stop-color="#5b4a3a"/>
        </linearGradient>
      </defs>
      <g role="img" aria-label="Photo of the valley glowing at sunrise">
        <path d="M0 0H373V250C250 280 120 290 0 300Z" fill="url(#sunPhoto)"/>
      </g>
      <path d="M0 300C120 290 250 280 373 250" fill="none" stroke="var(--accent)" stroke-width="8"/>
    </svg>
    <div role="img" aria-label="Round photo of a balloon against a blue sky" class="photo-ring" style="left:40px;top:140px;width:100px;height:100px;background:radial-gradient(circle,#9fc6e6,#3f7f4a)"></div>
    <div role="img" aria-label="Round photo of guests in a balloon basket" class="photo-ring" style="left:180px;top:60px;width:150px;height:150px;background:linear-gradient(160deg,#d7dde4,#8a6a52)"></div>
    <div class="layer" style="top:340px">
      <div class="feature"><h3>Weight Flexibility</h3><p>Every guest is welcome; simply tell us your weight at booking so we can balance the basket.</p></div>
      <div class="feature"><h3>Daily Flights</h3><p>Flights lift off at sunrise every day over the valley, followed by a relaxed champagne breakfast at a local restaurant.</p></div>
      <div class="feature"><h3>Digital Photo Package</h3><p>Add a digital photo package to keep the best moments of your flight to share with friends and family.</p></div>
    </div>
    <div class="bar bar--dark"><span class="phone-icon" style="background:var(--accent)"></span>vellarayballooning.example</div>
  </article>
</section>

</body>
</html>
```